Fahrzeugbeschriftung für einen Hofladen
Zielgruppe
Biologische Produkte an den Endverbraucher vermarkten. Vorallem Kartoffel, Eier und Getreide.
24 h Hofladen
Aufgabenstellung
ansprechendes Design mit unseren Logo
Es soll das vorhandene Logo + Telfonnummer,Ort und Homepage oben stehn.
KL Lastwiesel R8 Kastenwagen (In Fahrtrichtung links Befindet sich auf der Seite ein Lufthutze)

```html
<!DOCTYPE html>
<html lang="de">
<head>
<meta charset="utf-8">
<title>Grünhof Linde – Fahrzeugbeschriftung</title>
<link href="https://fonts.googleapis.com/css2?family=Open+Sans:wght@400;600;700&display=swap" rel="stylesheet">
<style>
  :root {
    --green: #b5c334;
    --taupe: #716762;
    --paper: #ffffff;
    --text-dark: #3b3735;
    --text-light: #f4f2f0;
  }
  html, body {
    margin: 0;
    padding: 0;
    width: 1200px;
    height: 728px;
    overflow: hidden;
    background: var(--paper);
  }
  .wrap-panel {
    position: relative;
    width: 1200px;
    height: 728px;
    font-family: "Open Sans", Arial, sans-serif;
  }
  .brand {
    position: absolute;
    left: 110px;
    top: 150px;
    display: flex;
    align-items: center;
    gap: 18px;
  }
  .brand-mark {
    width: 34px;
    height: 34px;
    border-radius: 50%;
    background: var(--green);
  }
  .brand-name {
    font-size: 78px;
    font-weight: 400;
    color: var(--taupe);
    line-height: 1;
    letter-spacing: 0.5px;
  }
  .contact {
    position: absolute;
    left: 790px;
    top: 118px;
    color: var(--text-dark);
  }
  .contact-phone {
    font-size: 42px;
    font-weight: 700;
    color: var(--green);
    margin: 0 0 14px;
    letter-spacing: 0.5px;
  }
  .contact-address {
    margin: 0 0 0 46px;
    font-size: 22px;
    line-height: 1.5;
    font-style: normal;
  }
  .livery-area {
    position: absolute;
    left: 60px;
    top: 380px;
    width: 1080px;
    height: 260px;
    background: linear-gradient(180deg, var(--green) 0%, var(--taupe) 60%, var(--taupe) 100%);
  }
  .web {
    position: absolute;
    left: 560px;
    top: 520px;
    margin: 0;
    font-size: 34px;
    font-weight: 400;
    line-height: 1.2;
    color: var(--text-light);
    letter-spacing: 0.5px;
  }
</style>
</head>
<body>
<main class="wrap-panel">
  <div class="brand">
    <span class="brand-mark"></span>
    <span class="brand-name">Grünhof Linde</span>
  </div>

  <div class="contact">
    <p class="contact-phone">02813/57214</p>
    <address class="contact-address">
      Grünhof Linde<br>
      Weidenweg 7<br>
      3572 Hollerbach
    </address>
  </div>

  <div class="livery-area" role="img" aria-label="Geschwungene Zierbänder in Grün und Taupe mit schwarzem Seitenstreifen"></div>

  <p class="web">www.gruenhoflinde.at</p>
</main>
</body>
</html>
```